Medical Marijuana Service in the Bay Area

This is for a business card design that is going to be making medical marijuana deliveries in the bay area. The name of the the business is "Silverpine Herbal Wellness". I would like to have a modern feel and showing us as a medical marijuana company but at the same time discrete about it. I'm trying to target more sophisticated clients.

Industry/Entity Type

Medical

Contact Information for Business Card

Would like people to know it is for medical marijuana but in a discrete way.

```html
<!DOCTYPE html>
<html lang="en">
<head>
<meta charset="utf-8">
<title>Silverpine Herbal Wellness — Business Card</title>
<link rel="stylesheet" href="https://fonts.googleapis.com/css2?family=Oswald:wght@300;400;500;600&display=swap">
<style>
  :root {
    --backdrop: #d9d9d9;
    --card-black: #1b1b1b;
    --brand-green: #57b03a;
    --muted-grey: #3a3a3a;
    --ink-dark: #1c1c1c;
    --text-light: #f2f2f2;
  }
  * { box-sizing: border-box; margin: 0; padding: 0; }
  html, body {
    width: 1200px; height: 1200px; overflow: hidden;
    background: var(--backdrop);
    font-family: "Oswald", "Arial Narrow", sans-serif;
  }
  .canvas {
    width: 1200px; height: 1200px;
    display: flex; flex-direction: column;
    align-items: center; justify-content: center; gap: 80px;
  }
  .card {
    position: relative;
    width: 700px; height: 400px;
    background: var(--card-black);
    overflow: hidden;
    box-shadow: 0 10px 30px rgba(0,0,0,0.25);
  }

  /* Front */
  .front .business-name {
    position: absolute; left: 40px; top: 34px;
    color: var(--brand-green);
    font-size: 46px; font-weight: 400; letter-spacing: 1px;
    text-transform: uppercase; line-height: 1;
  }
  .front .contact-bars {
    position: absolute; right: 0; top: 190px;
    display: flex; flex-direction: column; align-items: flex-end; gap: 34px;
  }
  .front .contact-bar {
    background: var(--brand-green);
    color: var(--text-light);
    font-size: 22px; font-weight: 400; letter-spacing: 1px;
    text-transform: uppercase;
    padding: 6px 24px 6px 18px;
    line-height: 1.3;
  }
  .front .contact-bar.phone { width: 290px; }
  .front .contact-bar.email { width: 380px; font-size: 17px; padding-top: 9px; padding-bottom: 9px; }
  .front .tagline {
    position: absolute; left: 40px; right: 40px; bottom: 22px;
    color: var(--muted-grey);
    font-size: 15px; font-weight: 300; letter-spacing: 12px;
    text-transform: uppercase; white-space: nowrap;
  }

  /* Back */
  .back .green-band {
    position: absolute; top: 0; bottom: 0; left: 140px; width: 420px;
    background: var(--brand-green);
  }
  .back .logotype {
    position: absolute; left: 172px; top: 96px;
    color: var(--ink-dark); text-transform: uppercase; line-height: 1;
  }
  .back .logotype .word-main {
    display: block; font-size: 64px; font-weight: 500; letter-spacing: 2px;
  }
  .back .logotype .word-sub {
    display: block; font-size: 40px; font-weight: 400; letter-spacing: 2px; margin-top: 6px;
  }
  .back .logotype .tagline {
    display: block; font-size: 15px; font-weight: 300; letter-spacing: 2px; margin-top: 10px;
    color: #2c4a22;
  }
</style>
</head>
<body>
  <main class="canvas">
    <section class="card front" aria-label="Business card front">
      <h1 class="business-name">Silverpine Herbal Wellness</h1>
      <div class="contact-bars">
        <p class="contact-bar phone">Phone: (415) 555-0142</p>
        <p class="contact-bar email">hello@silverpineherbal.com</p>
      </div>
      <p class="tagline">Medical Collective Delivery Service</p>
    </section>

    <section class="card back" aria-label="Business card back">
      <div class="green-band"></div>
      <h2 class="logotype">
        <span class="word-main">Silverpine</span>
        <span class="word-sub">Herbal Wellness</span>
        <span class="tagline">Medical Collective Delivery Service</span>
      </h2>
    </section>
  </main>
</body>
</html>
```